Reliable and clean label for a natural product!

We would like to have a label design for our CBD SOFT GEL CAPSULES . We are a business family and believe in the power of natural healing. In this label we would like to show a reliable, natural and feminine product mainly.

Font styles to use
Serif
Sans Serif

Colors

Designer to choose colors to be used in the design.

```html
<!DOCTYPE html>
<html lang="es">
<head>
<meta charset="utf-8">
<title>Hojaverde – Capsulas Aceite de CBD</title>
<link href="https://fonts.googleapis.com/css2?family=Barlow+Condensed:wght@400;600&display=swap" rel="stylesheet">
<style>
  :root{
    --page:#f7f3f2;
    --label-green:#b6d98f;
    --label-green-light:#c4e1a1;
    --leaf-tint:rgba(255,255,255,0.22);
    --ink:#ffffff;
    --badge:#e2837a;
  }
  *{margin:0;padding:0;box-sizing:border-box}
  html,body{width:1200px;height:1094px;overflow:hidden;background:var(--page)}
  .canvas{position:relative;width:1200px;height:1094px}
  .label{
    position:absolute;left:100px;top:166px;width:1000px;height:760px;
    background:linear-gradient(90deg,var(--label-green) 0%,var(--label-green-light) 50%,var(--label-green) 100%);
    overflow:hidden;color:var(--ink);
  }
  .leaf-art{
    position:absolute;left:386px;top:440px;width:380px;height:320px;
    background:radial-gradient(ellipse at 50% 55%,var(--leaf-tint) 0%,rgba(255,255,255,0.08) 60%,rgba(255,255,255,0) 75%);
  }
  .brand{
    position:absolute;left:0;right:0;top:124px;text-align:center;
    font-family:"Barlow Condensed",sans-serif;font-weight:600;font-size:48px;letter-spacing:0.5px;
  }
  .product{position:absolute;left:222px;top:300px;font-family:"Barlow Condensed",sans-serif}
  .product-type{font-size:38px;font-weight:400;letter-spacing:1px;line-height:1}
  .product-name{font-size:54px;font-weight:600;letter-spacing:1.5px;line-height:1.1;margin-top:8px}
  .divider{width:86px;height:3px;background:var(--ink);margin-top:46px}
  .specs{list-style:none;margin-top:16px;font-size:25px;letter-spacing:1px;line-height:41px}
  .count{position:absolute;left:222px;top:652px;font-family:"Barlow Condensed",sans-serif;font-size:30px;letter-spacing:1.5px}
  .dose-badge{
    position:absolute;left:613px;top:488px;width:136px;height:272px;
    background:var(--badge);border-top-left-radius:22px;
    font-family:"Barlow Condensed",sans-serif;text-align:center;padding-top:14px;
  }
  .dose-value{font-size:66px;font-weight:400;line-height:1}
  .dose-unit{font-size:17px;letter-spacing:0.5px;line-height:1.15;margin-top:8px}
</style>
</head>
<body>
<div class="canvas">
  <section class="label">
    <div class="leaf-art" role="img" aria-label="Faint decorative leaves"></div>
    <p class="brand">Hojaverde</p>
    <div class="product">
      <p class="product-type">CAPSULAS</p>
      <h1 class="product-name">ACEITE DE CBD</h1>
      <div class="divider"></div>
      <ul class="specs">
        <li>HEMP OIL</li>
        <li>EXTRACT CAPSULES</li>
        <li>FULL SPECTRUM</li>
      </ul>
    </div>
    <p class="count">30 CAPSULES</p>
    <div class="dose-badge">
      <p class="dose-value">25</p>
      <p class="dose-unit">MG CBD<br>PER CAPSULE</p>
    </div>
  </section>
</div>
</body>
</html>
```